SaaS startup seeking website design and build on Vornix.io

Need a website designed and built on Vornix.io for a new SaaS startup called PeakMoor (logo provided).

***The winning designer will be provided with a login to our Vornix.io subscription to deploy the design - please only submit a design if you are familiar with the Vornix platform. ***

The business will be selling a cloud-based system for customer success management; a tool to ensure SaaS businesses successfully onboard, retain for renewals, upsell and cross-sell to existing customers. Logo and colour guide provided, pages required in the design:
Home,
Tour,
Pricing,
Blog,
Contact

Require buttons/ forms for
Login,
Sign-up for Trial,
Sign-up for Newsletter,
Request Demo,
Contact Us.

The winning designer will be provided with a login to our Vornix.io subscription to deploy the design - please only submit a design if you are familiar with the Vornix platform. Draft designs submitted on trial vornix accounts will also be considered.

Seek inspiration and placeholder content from https://tallowbrim.net/
https://www.quimerra.com/
https://fernwhistle.com/

Target Market(s)

SaaS companies

Coding

Coded - Design and coding required

Number of Pages Required

1 page

```html
<!DOCTYPE html>
<html lang="en">
<head>
<meta charset="utf-8">
<title>PeakMoor – Customer Success Platform</title>
<link rel="stylesheet" href="https://fonts.googleapis.com/css2?family=Titillium+Web:wght@400;600&family=Arimo:wght@400;700&family=Barlow:wght@500;600&display=swap">
<style>
:root{
  --blue:#2b8ad6;
  --blue-deep:#1a6acb;
  --navy:#243a63;
  --navy-dark:#26416b;
  --ink:#2a3f62;
  --text:#5d6675;
  --muted:#8a93a2;
  --line:#e3e6ea;
  --tint:#f3f4f6;
  --tick:#2b8ad6;
  --white:#fff;
}
*{box-sizing:border-box;margin:0;padding:0}
html,body{width:1200px;height:4175px;overflow:hidden}
body{position:relative;font-family:"Arimo",Arial,sans-serif;color:var(--text);background:var(--white)}
.btn{position:absolute;display:flex;align-items:center;justify-content:center;font-family:"Barlow",sans-serif;font-weight:600;text-transform:uppercase;border-radius:30px;font-size:13px;letter-spacing:.3px}

/* header */
.site-header{position:absolute;left:0;top:0;width:1200px;height:110px;background:var(--white)}
.brand{position:absolute;left:174px;top:28px;display:flex;align-items:center;gap:10px;font-family:"Titillium Web",sans-serif;font-weight:600;font-size:42px;color:var(--navy);line-height:1}
.brand-dot{width:16px;height:16px;border-radius:50%;background:var(--blue)}
.nav-link{position:absolute;top:47px;font-family:"Barlow",sans-serif;font-weight:600;font-size:13px;color:var(--navy)}
.btn-login{left:834px;top:37px;width:92px;height:36px;border:2px solid var(--blue);color:var(--blue)}
.btn-signup{left:934px;top:37px;width:93px;height:36px;background:var(--navy);color:var(--white)}

/* hero */
.hero{position:absolute;left:0;top:110px;width:1200px;height:650px;background:linear-gradient(115deg,#1663c7 0%,#2b8ad6 55%,#3aa3e6 100%);clip-path:polygon(0 0,100% 0,100% 580px,50% 650px,0 580px)}
.hero-title{position:absolute;left:0;width:1200px;top:35px;text-align:center;font-family:"Titillium Web",sans-serif;font-weight:400;font-size:36px;line-height:48px;color:var(--white)}
.hero-sub{position:absolute;left:0;width:1200px;top:140px;text-align:center;font-family:"Barlow",sans-serif;font-weight:500;font-size:16px;color:var(--white)}
.signup-form{position:absolute;left:272px;top:185px;width:656px;height:49px;background:var(--white);border-radius:30px;overflow:hidden}
.signup-form span{position:absolute;left:22px;top:17px;font-size:12px;color:var(--text)}
.signup-form .go{position:absolute;right:0;top:0;width:122px;height:49px;background:var(--navy);color:var(--white);display:flex;align-items:center;justify-content:center;font-family:"Barlow",sans-serif;font-weight:600;font-size:13px}
.hero-screen{position:absolute;left:348px;top:290px;width:504px;height:420px;border-radius:14px;background:linear-gradient(160deg,#ffffff 0%,#e9eefa 60%,#c9d6f3 100%);border:10px solid #d9dde3}

/* press */
.press{position:absolute;left:174px;top:830px;width:853px;display:flex;justify-content:space-between;align-items:center;font-family:"Titillium Web",sans-serif;font-weight:600;font-size:22px;color:#9aa0a8}

/* features */
.feature-title{position:absolute;font-family:"Titillium Web",sans-serif;font-weight:600;font-size:32px;color:var(--ink)}
.feature-copy{position:absolute;width:360px;font-size:13px;line-height:25px;color:var(--text)}
.shot{position:absolute;border:1px solid #d7dbe1;border-radius:4px;background:#f6f7f9;box-shadow:0 2px 8px rgba(0,0,0,.06)}
.shot .bar{height:28px;padding:10px 12px;display:flex;gap:5px}
.shot .bar i{width:7px;height:7px;border-radius:50%;background:#c8ccd2}
.shot .view{position:absolute;left:10px;right:10px;top:30px;bottom:10px}
.checks{position:absolute;display:flex;gap:36px;font-size:12px;color:var(--text)}
.checks span{display:flex;align-items:center;gap:8px}
.divider{position:absolute;left:174px;width:853px;height:1px;background:var(--line)}
.item{position:absolute;width:440px;height:80px}
.item .ico{position:absolute;left:0;top:0;width:70px;height:70px;border-radius:50%;display:flex;align-items:center;justify-content:center}
.item .ico.light{background:var(--blue)}
.item .ico.dark{background:var(--navy)}
.item h4{position:absolute;left:87px;top:2px;font-family:"Titillium Web",sans-serif;font-weight:600;font-size:15px;color:var(--navy-dark)}
.item p{position:absolute;left:87px;top:28px;width:300px;font-size:11.5px;line-height:22px;color:var(--text)}

/* pricing */
.pricing{position:absolute;left:0;top:2498px;width:1200px;height:632px;background:var(--tint)}
.section-title{position:absolute;left:0;width:1200px;text-align:center;font-family:"Titillium Web",sans-serif;font-weight:600;font-size:36px;color:var(--ink)}
.section-sub{position:absolute;left:0;width:1200px;text-align:center;font-family:"Titillium Web",sans-serif;font-weight:400;font-size:20px;color:var(--blue)}
.plan{position:absolute;top:175px;width:267px;height:384px;background:var(--white);border-radius:4px;box-shadow:0 2px 10px rgba(0,0,0,.08);text-align:center}
.plan h3{position:absolute;left:0;width:267px;top:22px;line-height:36px;font-family:"Titillium Web",sans-serif;font-weight:600;font-size:24px;color:var(--ink)}
.plan .note{position:absolute;left:16px;width:235px;top:62px;font-family:"Titillium Web",sans-serif;font-size:12.5px;line-height:19px;color:var(--blue)}
.plan .price{position:absolute;left:0;width:267px;top:104px;font-family:"Titillium Web",sans-serif;font-weight:600;font-size:56px;line-height:56px;color:var(--blue)}
.plan.mid .price{color:var(--navy)}
.plan .price sup{font-size:20px;vertical-align:top;position:relative;top:-6px}
.plan .price small{font-size:12px;font-weight:400}
.plan ul{position:absolute;left:45px;top:173px;list-style:none;text-align:left;font-size:12.5px;color:var(--text)}
.plan li{display:flex;align-items:center;gap:16px;height:36px}
.plan .btn{left:68px;top:301px;width:131px;height:44px;background:var(--blue);color:var(--white)}
.plan.mid .btn{background:var(--navy)}

/* contact */
.field-label{position:absolute;left:349px;font-size:12px;color:var(--text)}
.field{position:absolute;border:1px solid #cfd4da;background:var(--white);font-size:11px;color:var(--muted);padding:14px 14px}
.btn-send{left:527px;top:3590px;width:146px;height:44px;background:var(--blue);color:var(--white);font-size:13px}

/* cta */
.cta{position:absolute;left:0;top:3689px;width:1200px;height:266px;background:var(--blue)}
.cta h2{position:absolute;left:0;width:1200px;top:50px;text-align:center;font-family:"Titillium Web",sans-serif;font-weight:600;font-size:34px;color:var(--white)}
.cta p{position:absolute;left:0;width:1200px;top:106px;text-align:center;font-family:"Titillium Web",sans-serif;font-size:17px;color:var(--white)}
.cta .btn{top:157px;width:163px;height:45px;text-transform:none;font-family:"Titillium Web",sans-serif;font-size:17px}
.cta .primary{left:431px;background:var(--navy);color:var(--white)}
.cta .ghost{left:607px;border:2px solid var(--white);color:var(--white)}

/* footer */
.site-footer{position:absolute;left:0;top:3955px;width:1200px;height:220px;background:var(--navy-dark);color:var(--white)}
.copyright{position:absolute;left:179px;top:58px;font-size:11.5px}
.social{position:absolute;left:181px;top:88px;display:flex;gap:10px}
.social i{width:12px;height:12px;border-radius:50%;background:var(--white)}
.foot-col{position:absolute;top:52px}
.foot-col h5{font-family:"Titillium Web",sans-serif;font-weight:600;font-size:18px;margin-bottom:14px}
.foot-col a{display:block;color:var(--white);text-decoration:none;font-size:12px;line-height:28px}
</style>
</head>
<body>

<header class="site-header">
  <div class="brand"><span class="brand-dot"></span>PeakMoor</div>
  <a class="nav-link" style="left:580px">FEATURES</a>
  <a class="nav-link" style="left:693px">PRICING</a>
  <a class="nav-link" style="left:790px">FAQ</a>
  <a class="btn btn-login">Login</a>
  <a class="btn btn-signup">Sign up</a>
</header>

<section class="hero">
  <h1 class="hero-title">Spark Interest: What Makes Your<br>product desirable?</h1>
  <p class="hero-sub">Use this space to tell the customer how your product works &amp; why it is different.</p>
  <div class="signup-form"><span>Enter Your Email Id:</span><div class="go">GET STARTED</div></div>
  <div class="hero-screen" role="img" aria-label="Product dashboard with charts, stats and sidebar navigation"></div>
</section>

<div class="press">
  <span>Venture Weekly</span><span>Ledgerline</span><span>Capstone</span><span>Growth 300</span><span>The Daily Mast</span>
</div>

<!-- feature 1 -->
<h2 class="feature-title" style="left:174px;top:1058px">Your great feature</h2>
<p class="feature-copy" style="left:174px;top:1118px">Use this section to show off one of your features in great detail. You can add a list of bullet-points with custom icons, checkmarks and a product display.</p>
<div class="checks" style="left:174px;top:1226px">
  <span><svg width="12" height="10" viewBox="0 0 12 10"><path d="M1 5l3.5 3.5L11 1.5" fill="none" stroke="#2b8ad6" stroke-width="2"/></svg>Looks great</span>
  <span><svg width="12" height="10" viewBox="0 0 12 10"><path d="M1 5l3.5 3.5L11 1.5" fill="none" stroke="#2b8ad6" stroke-width="2"/></svg>Easy to use</span>
  <span><svg width="12" height="10" viewBox="0 0 12 10"><path d="M1 5l3.5 3.5L11 1.5" fill="none" stroke="#2b8ad6" stroke-width="2"/></svg>Try it yourself!</span>
</div>
<div class="shot" style="left:587px;top:973px;width:440px;height:373px">
  <div class="bar"><i></i><i></i><i></i></div>
  <div class="view" role="img" aria-label="Dashboard screen with line charts, bar charts and gauges" style="background:linear-gradient(90deg,#1f4fc4 0 16%,#fff 16%)"></div>
</div>

<div class="divider" style="top:1400px"></div>

<!-- feature 2 -->
<div class="shot" style="left:174px;top:1505px;width:438px;height:370px">
  <div class="bar"><i></i><i></i><i></i></div>
  <div class="view" role="img" aria-label="Analytics screen with stat tiles, donut charts and bar charts" style="background:linear-gradient(180deg,#2b6fdc 0 6%,#f2f4f9 6%)"></div>
</div>
<h2 class="feature-title" style="left:650px;top:1438px">Your great feature</h2>
<p class="feature-copy" style="left:650px;top:1498px">Use this section to show off one of your features in great detail. You can add a list of bullet-points with custom icons, checkmarks and a product display.</p>
<div class="item" style="left:650px;top:1600px">
  <div class="ico light"><svg width="28" height="22" viewBox="0 0 28 22"><rect x="4" y="2" width="20" height="13" rx="1" fill="none" stroke="#fff" stroke-width="2"/><path d="M1 18h26" stroke="#fff" stroke-width="2.5"/></svg></div>
  <h4>Product display</h4>
  <p>To the right (or left) of your feature text, you can add a product display just like the ones in the hero section.</p>
</div>
<div class="item" style="left:650px;top:1702px">
  <div class="ico dark"><svg width="26" height="20" viewBox="0 0 26 20"><g fill="#fff"><circle cx="3" cy="3" r="2.2"/><circle cx="3" cy="10" r="2.2"/><circle cx="3" cy="17" r="2.2"/><rect x="8" y="1.5" width="17" height="3"/><rect x="8" y="8.5" width="17" height="3"/><rect x="8" y="15.5" width="17" height="3"/></g></svg></div>
  <h4>This cool list with icons</h4>
  <p>You can toggle this list and any other part of the feature section to adjust it to your needs.</p>
</div>
<div class="item" style="left:650px;top:1804px">
  <div class="ico light"><svg width="20" height="28" viewBox="0 0 20 28"><path d="M10 2a8 8 0 0 0-5 14v4h10v-4a8 8 0 0 0-5-14z" fill="none" stroke="#fff" stroke-width="2"/><path d="M6 24h8" stroke="#fff" stroke-width="2"/></svg></div>
  <h4>A list of checkmarks</h4>
  <p>You can also add a little list of short text snippets with green checkmarks in front of them.</p>
</div>

<div class="divider" style="top:1942px"></div>

<!-- feature 3 -->
<h2 class="feature-title" style="left:174px;top:1980px">Your great feature</h2>
<p class="feature-copy" style="left:174px;top:2040px">Use this section to show off one of your features in great detail. You can add a list of bullet-points with custom icons, checkmarks and a product display.</p>
<div class="item" style="left:174px;top:2142px">
  <div class="ico light"><svg width="22" height="28" viewBox="0 0 22 28"><path d="M2 2h12l6 6v18H2z" fill="none" stroke="#fff" stroke-width="2"/><path d="M6 14h10M6 19h10" stroke="#fff" stroke-width="2"/></svg></div>
  <h4>Product display</h4>
  <p>To the right (or left) of your feature text, you can add a product display just like the ones in the hero section.</p>
</div>
<div class="item" style="left:174px;top:2244px">
  <div class="ico dark"><svg width="26" height="26" viewBox="0 0 26 26"><rect x="3" y="9" width="13" height="14" rx="2" fill="none" stroke="#fff" stroke-width="2"/><rect x="10" y="3" width="13" height="14" rx="2" fill="none" stroke="#fff" stroke-width="2"/></svg></div>
  <h4>This cool list with icons</h4>
  <p>You can toggle this list and any other part of the feature section to adjust it to your needs.</p>
</div>
<div class="item" style="left:174px;top:2346px">
  <div class="ico light"><svg width="26" height="26" viewBox="0 0 26 26"><circle cx="13" cy="13" r="7" fill="none" stroke="#fff" stroke-width="5" stroke-dasharray="4 3.3"/><circle cx="13" cy="13" r="3" fill="#fff"/></svg></div>
  <h4>A list of checkmarks</h4>
  <p>You can also add a little list of short text snippets with green checkmarks in front of them.</p>
</div>
<div class="shot" style="left:587px;top:2047px;width:440px;height:370px">
  <div class="bar"><i></i><i></i><i></i></div>
  <div class="view" role="img" aria-label="Dashboard screen with navy sidebar, area chart and data tables" style="background:linear-gradient(90deg,#1c2670 0 18%,#fff 18%)"></div>
</div>

<!-- pricing -->
<section class="pricing">
  <h2 class="section-title" style="top:48px">Simple, Transparent Pricing</h2>
  <p class="section-sub" style="top:104px">Always know what you'll Pay</p>

  <div class="plan" style="left:174px">
    <h3>Small</h3>
    <p class="note">This layout looks best with 2-3 tiers</p>
    <div class="price"><sup>$</sup>49<small>/mo</small></div>
    <ul>
      <li><svg width="12" height="10" viewBox="0 0 12 10"><path d="M1 5l3.5 3.5L11 1.5" fill="none" stroke="#2b8ad6" stroke-width="2"/></svg>Your great feature</li>
      <li><svg width="12" height="10" viewBox="0 0 12 10"><path d="M1 5l3.5 3.5L11 1.5" fill="none" stroke="#2b8ad6" stroke-width="2"/></svg>Another important thing</li>
      <li><svg width="12" height="10" viewBox="0 0 12 10"><path d="M1 5l3.5 3.5L11 1.5" fill="none" stroke="#2b8ad6" stroke-width="2"/></svg>You can add many more</li>
    </ul>
    <a class="btn">Signup</a>
  </div>

  <div class="plan mid" style="left:466px">
    <h3>Growth</h3>
    <p class="note">If you have more tiers or lots of features, try the table.</p>
    <div class="price"><sup>$</sup>99<small>/mo</small></div>
    <ul>
      <li><svg width="12" height="10" viewBox="0 0 12 10"><path d="M1 5l3.5 3.5L11 1.5" fill="none" stroke="#2b8ad6" stroke-width="2"/></svg>Your great feature</li>
      <li><svg width="12" height="10" viewBox="0 0 12 10"><path d="M1 5l3.5 3.5L11 1.5" fill="none" stroke="#2b8ad6" stroke-width="2"/></svg>Another important thing</li>
      <li><svg width="12" height="10" viewBox="0 0 12 10"><path d="M1 5l3.5 3.5L11 1.5" fill="none" stroke="#2b8ad6" stroke-width="2"/></svg>You can add many more</li>
    </ul>
    <a class="btn">Signup</a>
  </div>

  <div class="plan" style="left:759px">
    <h3>Large</h3>
    <p class="note">You can set the color of these boxes in the Tier BG settings.</p>
    <div class="price"><sup>$</sup>199<small>/mo</small></div>
    <ul>
      <li><svg width="12" height="10" viewBox="0 0 12 10"><path d="M1 5l3.5 3.5L11 1.5" fill="none" stroke="#2b8ad6" stroke-width="2"/></svg>Your great feature</li>
      <li><svg width="12" height="10" viewBox="0 0 12 10"><path d="M1 5l3.5 3.5L11 1.5" fill="none" stroke="#2b8ad6" stroke-width="2"/></svg>Another important thing</li>
      <li><svg width="12" height="10" viewBox="0 0 12 10"><path d="M1 5l3.5 3.5L11 1.5" fill="none" stroke="#2b8ad6" stroke-width="2"/></svg>You can add many more</li>
    </ul>
    <a class="btn">Signup</a>
  </div>
</section>

<!-- contact -->
<h2 class="section-title" style="top:3162px">Contact us</h2>
<p class="section-sub" style="top:3222px">Got any questions? Don't hesitate to reach out.</p>
<label class="field-label" style="top:3280px">Full Name</label>
<div class="field" style="left:348px;top:3301px;width:504px;height:44px">Jane Doe</div>
<label class="field-label" style="top:3366px">Email Address</label>
<div class="field" style="left:348px;top:3387px;width:245px;height:43px">jane.doe@mailbox.test</div>
<label class="field-label" style="top:3366px;left:608px">Phone (Optional)</label>
<div class="field" style="left:607px;top:3387px;width:245px;height:43px">(000) 000-0000</div>
<label class="field-label" style="top:3450px">Your Message</label>
<div class="field" style="left:348px;top:3470px;width:504px;height:95px"></div>
<a class="btn btn-send">Send Message</a>

<!-- cta -->
<section class="cta">
  <h2>Ready to get started?</h2>
  <p>Contact us or sign up now.</p>
  <a class="btn primary">Get Started</a>
  <a class="btn ghost">Contact Us</a>
</section>

<footer class="site-footer">
  <p class="copyright">© 2020 My Company</p>
  <div class="social"><i></i><i></i><i></i></div>
  <div class="foot-col" style="left:530px"><h5>Product</h5><a>Features</a><a>Pricing</a><a>Tour</a></div>
  <div class="foot-col" style="left:696px"><h5>Company</h5><a>About</a><a>Team</a><a>Blog</a></div>
  <div class="foot-col" style="left:855px"><h5>Legal</h5><a>Terms of Service</a><a>Privacy Policy</a><a>GDPR Policy</a></div>
</footer>

</body>
</html>
```